Industrial Project Sign

We need an eye catching (but professional) industrial project sign that will be very large (roughly 12' high x 18' wide). This sign will be highly visible from the adjacent high speed highway.

* The following needs to be at the bottom of the signage: Logo (uploaded), Name (Halvern Land Holdings, Inc.) (uploaded) and phone number (555)739-2864

*Name of Project - "Marrowfield Logistics Park"

* Text items
Land for Sale
Build to Suit
Zoning: Industrial (G I & L I)

* Interesting background that is eye catching

Good morning all,

We are considering all designers options as we go and are waiting for the final designs to come in by the 4th so that we can give each one a good look.   If you have any new designs, questions, further design options or any tweeks you want to do to current designs, please do so at this time.

Thanks to all of you for your submissions.

Industrial

```html
<!DOCTYPE html>
<html lang="en">
<head>
<meta charset="utf-8">
<title>Land for Sale – Halvern Land Holdings, Inc.</title>
<link rel="stylesheet" href="https://fonts.googleapis.com/css2?family=Alfa+Slab+One&family=Graduate&family=Roboto:wght@400;900&display=swap">
<style>
  :root {
    --sunburst-light: #fff27a;
    --sunburst-mid: #f7dc1e;
    --sunburst-deep: #e9b41c;
    --sale-red: #e31b2b;
    --outline-white: #ffffff;
    --steel-light: #f2f2f2;
    --steel-mid: #a9a9a9;
    --steel-dark: #4a4a4a;
    --ink-black: #000000;
    --panel-white: #ffffff;
    --brand-maroon: #7a1418;
    --brand-grey: #6d6d6d;
  }
  html, body {
    margin: 0;
    padding: 0;
    width: 1200px;
    height: 800px;
    overflow: hidden;
    background: #ffffff;
  }
  .sign {
    position: relative;
    width: 1200px;
    height: 800px;
    overflow: hidden;
  }
  .sign-art {
    position: absolute;
    inset: 0;
    display: block;
  }
  .headline-word {
    font-family: "Alfa Slab One", serif;
    fill: var(--sale-red);
    stroke: var(--outline-white);
    stroke-width: 5;
    paint-order: stroke fill;
  }
  .steel-text {
    font-family: "Graduate", serif;
    fill: url(#steel);
    stroke: var(--steel-dark);
    stroke-width: 2.5;
    paint-order: stroke fill;
  }
  .footer-phone {
    font-family: "Roboto", sans-serif;
    font-weight: 900;
    fill: var(--panel-white);
  }
  .footer-brand {
    font-family: "Roboto", sans-serif;
    font-weight: 400;
    fill: var(--brand-grey);
  }
</style>
</head>
<body>
<main class="sign">
  <svg class="sign-art" viewBox="0 0 1200 800" width="1200" height="800" xmlns="http://www.w3.org/2000/svg">
    <defs>
      <radialGradient id="sunburst" cx="50%" cy="40%" r="75%">
        <stop offset="0%" stop-color="var(--sunburst-light)"/>
        <stop offset="55%" stop-color="var(--sunburst-mid)"/>
        <stop offset="100%" stop-color="var(--sunburst-deep)"/>
      </radialGradient>
      <linearGradient id="steel" x1="0" y1="0" x2="0" y2="1">
        <stop offset="0%" stop-color="var(--steel-light)"/>
        <stop offset="45%" stop-color="var(--steel-mid)"/>
        <stop offset="60%" stop-color="var(--steel-light)"/>
        <stop offset="100%" stop-color="var(--steel-mid)"/>
      </linearGradient>
      <filter id="drop" x="-10%" y="-10%" width="130%" height="130%">
        <feDropShadow dx="5" dy="6" stdDeviation="4" flood-color="#000" flood-opacity="0.55"/>
      </filter>
    </defs>

    <rect class="backdrop" x="0" y="0" width="1200" height="671" fill="url(#sunburst)" role="img" aria-label="Yellow marbled texture with orange veins"/>

    <text class="steel-text" x="50" y="113" font-size="66" textLength="590" lengthAdjust="spacingAndGlyphs" filter="url(#drop)">BUILD TO SUIT</text>

    <g class="headline" transform="skewY(-16.8)" filter="url(#drop)">
      <text class="headline-word" x="42" y="567" font-size="300" textLength="412" lengthAdjust="spacingAndGlyphs">LAND</text>
      <text class="headline-word" x="472" y="567" font-size="255" textLength="218" lengthAdjust="spacingAndGlyphs">FOR</text>
      <text class="headline-word" x="704" y="567" font-size="210" textLength="453" lengthAdjust="spacingAndGlyphs">SALE</text>
    </g>

    <g class="zoning" text-anchor="end" filter="url(#drop)">
      <text class="steel-text" x="1158" y="430" font-size="64" textLength="342" lengthAdjust="spacingAndGlyphs">ZONING:</text>
      <text class="steel-text" x="1158" y="505" font-size="64" textLength="522" lengthAdjust="spacingAndGlyphs">INDUSTRIAL</text>
      <text class="steel-text" x="1158" y="580" font-size="64" textLength="260" lengthAdjust="spacingAndGlyphs">GI &amp; LI</text>
    </g>

    <rect class="footer-brand-panel" x="0" y="671" width="421" height="129" fill="var(--panel-white)"/>
    <rect class="footer-phone-panel" x="421" y="671" width="779" height="129" fill="var(--ink-black)"/>

    <rect class="brand-mark" x="22" y="706" width="58" height="58" fill="var(--brand-maroon)"/>
    <text class="footer-brand" x="96" y="744" font-size="21" textLength="308" lengthAdjust="spacingAndGlyphs">Halvern Land Holdings, Inc.</text>

    <text class="footer-phone" x="454" y="772" font-size="120" textLength="710" lengthAdjust="spacingAndGlyphs">(555)739-2864</text>
  </svg>
</main>
</body>
</html>
```